Popup Nightclub Grand Opening Flyer

We need to design a flyer for the grand opening of an upscale, exclusive nightclub called "Lanternfall". The design needs to be chic and exclusive. The background should be black and the text should primarily be white. We like minimalist designs.

Here is the text for the flyer
-
Velvetrope Atlanta Presents

Lanternfall (LOGO)

A Popup Nightclub Experience
For one night Only

Friday, October 18, 2013
Party begins at 9PM

INVITE ONLY

See invitation for location details
(Velvetrope Atlanta logo)

-
Examples we like

http://cdn2-b.brivelpost.com/sites/default/files/styles/image_content_width/hash/3d/fa/1472093815_4471_flyer.jpg?itok=R8kqWm2z

http://api.plovra.com/files/7Kqq-Tr82XXB3pQzJvmtR5HL2W719E4nbRtC6KLd4HsfM8Y2qTDK-VmjwDoNqLX4QBzTHD9nakRbVx3m-Pfq8htc3MDTWr5p4/2zelSaturdays.jpg

http://quenmar.com/wp-content/uploads/yootheme/widgetkit/gallery/2zel/2zel-gen_vroom4-01.jpg

Hi All, one thing that we are seeing that we don't like is on over emphasis on the phrase "a popup nightclub experience" please don't make this the largest thing on the flyer

Target Market(s)

Target market is 25-35 year olds who are affluent (rich) and like luxury brands

Requirements
Must have
• Dark Background
Nice to have
• Velvetrope Logo on the bottom
Modern text that isn't curvy
Should not have
• Curved text

```html
<!DOCTYPE html>
<html lang="en">
<head>
<meta charset="utf-8">
<title>Lanternfall Nightclub – Popup Opening</title>
<link rel="stylesheet" href="https://fonts.googleapis.com/css2?family=Archivo+Black&family=Jost:wght@300;400&display=swap">
<style>
  :root {
    --bg: #0b0b0b;
    --silhouette: #131313;
    --white: #ffffff;
    --silver-light: #f4f4f4;
    --silver-dark: #8f8f8f;
    --ring: #d6d6d6;
  }
  * { margin: 0; padding: 0; box-sizing: border-box; }
  html, body { width: 848px; height: 1200px; overflow: hidden; background: var(--bg); }
  .flyer {
    position: relative;
    width: 848px;
    height: 1200px;
    background: var(--bg);
    overflow: hidden;
    font-family: "Jost", sans-serif;
    color: var(--white);
  }

  .date, .start-time {
    position: absolute;
    left: 40px;
    font-family: "Archivo Black", sans-serif;
    text-transform: uppercase;
    letter-spacing: -2px;
    transform: scaleX(0.66);
    transform-origin: left top;
    white-space: nowrap;
    background: linear-gradient(180deg, var(--silver-dark) 0%, var(--silver-light) 100%);
    -webkit-background-clip: text;
    background-clip: text;
    color: transparent;
  }
  .date { top: 4px; font-size: 96px; line-height: 82px; }
  .start-time { top: 1080px; font-size: 88px; line-height: 100px; }

  .guests { position: absolute; background: var(--silhouette); }
  .guests--left {
    left: 42px; top: 528px; width: 258px; height: 600px;
    border-radius: 125px 125px 24px 24px;
  }
  .guests--right {
    left: 594px; top: 520px; width: 176px; height: 420px;
    border-radius: 88px 88px 24px 24px;
  }

  .mark-circle {
    position: absolute;
    left: 326px; top: 470px;
    width: 196px; height: 196px;
    border-radius: 50%;
    border: 24px solid var(--ring);
  }

  .club-name {
    position: absolute;
    left: 0; right: 0; top: 722px;
    text-align: center;
    font-weight: 300;
    font-size: 68px;
    line-height: 84px;
    letter-spacing: 0.11em;
    padding-left: 0.11em;
    text-transform: uppercase;
  }
  .club-type {
    position: absolute;
    left: 0; right: 0; top: 818px;
    text-align: center;
    font-weight: 400;
    font-size: 44px;
    line-height: 52px;
    letter-spacing: 0.15em;
    padding-left: 0.15em;
    text-transform: uppercase;
  }

  .tagline {
    position: absolute;
    left: 0; right: 0; top: 1056px;
    text-align: center;
    font-weight: 400;
    font-size: 21px;
    line-height: 30px;
  }

  .presenter {
    position: absolute;
    left: 274px; top: 1106px;
    display: flex;
    align-items: center;
  }
  .presenter-dot {
    width: 56px; height: 56px;
    border-radius: 50%;
    background: var(--white);
  }
  .presenter-rule {
    width: 2px; height: 52px;
    margin: 0 20px 0 32px;
    background: var(--white);
  }
  .presenter-name {
    font-weight: 400;
    color: var(--white);
    text-transform: uppercase;
  }
  .presenter-name .brand { display: block; font-size: 30px; line-height: 34px; letter-spacing: 0.04em; }
  .presenter-name .city { display: block; font-size: 13px; line-height: 18px; letter-spacing: 0.3em; margin-top: 4px; }
</style>
</head>
<body>
  <main class="flyer">
    <div class="guests guests--left" role="img" aria-label="Faint silhouette of a guest holding a drink"></div>
    <div class="guests guests--right" role="img" aria-label="Faint silhouette of a second guest"></div>

    <div class="date">Oct<br>18<br>Fri</div>

    <div class="mark-circle"></div>
    <h1 class="club-name">Lanternfall</h1>
    <p class="club-type">Nightclub</p>

    <p class="tagline">A Popup Nightclub Experience</p>

    <div class="start-time">9PM</div>

    <div class="presenter">
      <span class="presenter-dot"></span>
      <span class="presenter-rule"></span>
      <span class="presenter-name">
        <span class="brand">Velvetrope</span>
        <span class="city">Atlanta</span>
      </span>
    </div>
  </main>
</body>
</html>
```